Informational Business Handout needs Company Information

We have this informational handout that we would like to start handing out to clients; however, the original designer failed to include any of our company contact information. Our main request is that you redesign this card with the appropriate contact information as listed below. We would like the information/content that is currently on the card to be on the new design as well. Feel free to take liberty with the rest of the card design, or not. Please see the card specifications and our company contact information below.

Card details: 7 x 5 inches (17.78 x 12.5 cm). Cardstock.

Company Contact Details:
Dorian Maskell, JD
TrueMark, PLLC
538 E. Harlow Ave, Ste. 410, St. George, UT 84913
hello@truemark-example.com
(435) 555-0172

```html
<!DOCTYPE html>
<html lang="en">
<head>
<meta charset="utf-8">
<title>Third-Party Supplemental Needs Trust – TrueMark, PLLC</title>
<link rel="stylesheet" href="https://fonts.googleapis.com/css2?family=Montserrat:wght@500;600;700;800;900&display=swap">
<style>
  :root {
    --navy: #0e2561;
    --orange: #d44a23;
    --ink: #333333;
    --paper: #ffffff;
    --backdrop: #3b3b3b;
  }
  * { box-sizing: border-box; margin: 0; padding: 0; }
  html, body { width: 1200px; height: 1200px; overflow: hidden; background: var(--backdrop); }
  body { position: relative; font-family: "Montserrat", sans-serif; }

  .card {
    position: absolute; left: 30px; top: 200px;
    width: 1140px; height: 800px;
    background: var(--paper);
    overflow: hidden;
  }
  .card__shapes { position: absolute; inset: 0; width: 1140px; height: 800px; }

  .headline {
    position: absolute; left: 44px; top: 146px;
    color: var(--navy); font-weight: 900; font-size: 39px; line-height: 41px;
    letter-spacing: 0.5px; text-transform: uppercase; white-space: nowrap;
  }
  .intro {
    position: absolute; left: 44px; top: 236px;
    color: var(--ink); font-weight: 600; font-size: 22px; line-height: 27.5px;
    letter-spacing: 0.5px; white-space: nowrap;
  }
  .checklist-title {
    position: absolute; left: 46px; top: 334px;
    color: var(--navy); font-weight: 900; font-size: 31px; letter-spacing: 0.6px;
    text-transform: uppercase; white-space: nowrap;
  }
  .checklist { list-style: none; position: absolute; left: 46px; top: 0; width: 660px; }
  .checklist__item {
    position: absolute; left: 0; width: 660px;
    color: var(--ink); font-weight: 600; font-size: 21px; line-height: 23px; letter-spacing: 0.4px;
    padding-left: 40px; white-space: nowrap;
  }
  .checklist__item::before {
    content: ""; position: absolute; left: 0; top: 2px;
    width: 27px; height: 27px; border: 2.5px solid var(--navy); border-radius: 6px;
  }
  .closing {
    position: absolute; left: 52px; top: 578px;
    color: var(--navy); font-weight: 700; font-size: 19.5px; line-height: 21px; letter-spacing: 0.3px;
    white-space: nowrap;
  }
  .brand {
    position: absolute; left: 736px; top: 470px;
    color: var(--navy); font-weight: 600; font-size: 38px; letter-spacing: 9px;
  }
  .contact {
    position: absolute; left: 706px; top: 690px; color: var(--paper);
    font-style: normal; font-weight: 500; font-size: 16px; line-height: 19px;
    white-space: nowrap;
  }
  .contact__name { padding-left: 25px; margin-bottom: 10px; }
  .contact__row { display: flex; align-items: flex-start; gap: 8px; }
  .contact__row + .contact__row { margin-top: 9px; }
  .contact__row svg { flex: none; margin-top: 2px; }
  .contact__inline { align-items: center; }
  .contact__inline svg { margin-top: 0; }
  .contact__inline span { flex: none; }
  .contact__inline span + svg { margin-left: 10px; }
</style>
</head>
<body>
  <article class="card">
    <svg class="card__shapes" viewBox="0 0 1140 800" aria-hidden="true">
      <defs>
        <linearGradient id="cornerFade" x1="0" y1="1" x2="1" y2="0">
          <stop offset="0" stop-color="#d44a23"/>
          <stop offset="0.45" stop-color="#8a3d3c"/>
          <stop offset="1" stop-color="#0e2561"/>
        </linearGradient>
      </defs>
      <polygon points="0,0 342,0 0,147" fill="url(#cornerFade)"/>
      <polygon points="1140,513 1140,800 469,800" fill="var(--navy)"/>
    </svg>

    <h1 class="headline">Is a Third-Party Supplemental Needs<br>Trust Necessary for Your Estate Plan?</h1>

    <p class="intro">Will one of your intended beneficiaries, who has a physical or mental medical-<br>ly-recognized disability, be disqualified by the Social Security Administration<br>or other support should they receive any substantial financial gains?</p>

    <h2 class="checklist-title">Does the intended beneficiary…</h2>

    <ul class="checklist">
      <li class="checklist__item" style="top:392px">Currently receive or will be applying for Social<br>Security Income?</li>
      <li class="checklist__item" style="top:447px">Currently receive, or plan to apply for Medicaid?</li>
      <li class="checklist__item" style="top:485px">want to maintain or qualify for Social Security<br>Income and/or medicaid after benefitting from<br>an inheritance?</li>
    </ul>

    <p class="closing">If you have an intended beneficiary with a<br>recognized disability and you answered yes to any of<br>these questions, you should contact our office to<br>discuss whether a Third-Party Supplemental Needs<br>Trust is right for your estate plan.</p>

    <div class="brand">TRUEMARK</div>

    <address class="contact">
      <div class="contact__name">Dorian Maskell, JD | TrueMark, PLLC</div>
      <div class="contact__row">
        <svg width="17" height="22" viewBox="0 0 17 22" aria-hidden="true"><path d="M8.5 1C4.4 1 1.5 4 1.5 8c0 5 7 13 7 13s7-8 7-13c0-4-2.9-7-7-7z" fill="none" stroke="var(--orange)" stroke-width="2.5"/><circle cx="8.5" cy="8" r="2.5" fill="var(--orange)"/></svg>
        <span>538 E. Harlow Ave,<br>Ste. 410, St. George, UT 84913</span>
      </div>
      <div class="contact__row contact__inline">
        <svg width="17" height="12" viewBox="0 0 17 12" aria-hidden="true"><rect width="17" height="12" rx="1" fill="var(--orange)"/><path d="M1 1l7.5 6L16 1" fill="none" stroke="var(--navy)" stroke-width="1.5"/></svg>
        <span>hello@truemark-example.com</span>
        <svg width="16" height="16" viewBox="0 0 24 24" aria-hidden="true"><path d="M6.6 10.8a15.1 15.1 0 006.6 6.6l2.2-2.2a1 1 0 011-.25 11.4 11.4 0 003.6.6 1 1 0 011 1V20a1 1 0 01-1 1A17 17 0 013 4a1 1 0 011-1h3.5a1 1 0 011 1 11.4 11.4 0 00.6 3.6 1 1 0 01-.25 1z" fill="var(--orange)"/></svg>
        <span>(435) 555-0172</span>
      </div>
    </address>
  </article>
</body>
</html>
```